Need a business card created for my Heating and Air-conditioning business

We are a new Air Conditioning , Refrigeration and Heating business called Frost & Cinder HVAC/R - we do repairs, maintenance and installations.

Our motto is "Skilled Precision - Superior Value"

Information needed on the card:
Neil Fardon
778-555-4817
www.frosthvac-example.ca
info@frosthvac-example.ca

```html
<!DOCTYPE html>
<html lang="en">
<head>
<meta charset="utf-8">
<title>Frost &amp; Cinder HVAC/R — Business Card</title>
<link rel="stylesheet" href="https://fonts.googleapis.com/css2?family=Open+Sans:ital,wght@0,400;0,600;1,700&display=swap">
<style>
  :root {
    --backdrop: #58585a;
    --card: #000000;
    --ink: #ffffff;
    --band-blue: #7ab0e0;
    --band-light: #ffffff;
  }
  html, body {
    margin: 0;
    padding: 0;
    width: 1200px;
    height: 960px;
    overflow: hidden;
    background: var(--backdrop);
    font-family: "Open Sans", Arial, sans-serif;
    color: var(--ink);
  }
  .stage { position: relative; width: 1200px; height: 960px; }
  .card {
    position: absolute;
    width: 748px;
    height: 427px;
    background: var(--card);
    border-radius: 32px;
    overflow: hidden;
  }
  .card--front { left: 110px; top: 43px; }
  .card--back  { left: 314px; top: 508px; }

  .brand { position: absolute; display: flex; align-items: center; gap: 18px; }
  .brand__ring {
    border: 2px solid var(--ink);
    border-radius: 50%;
    flex: none;
  }
  .brand__name {
    font-weight: 600;
    color: var(--ink);
    white-space: nowrap;
    letter-spacing: 0.5px;
  }
  .card--front .brand { left: 32px; top: 55px; }
  .card--front .brand__ring { width: 150px; height: 150px; }
  .card--front .brand__name { font-size: 26px; }
  .card--back .brand { left: 180px; top: 112px; }
  .card--back .brand__ring { width: 190px; height: 190px; }
  .card--back .brand__name { font-size: 30px; }

  .name-band {
    position: absolute;
    left: 0; top: 246px;
    width: 748px; height: 51px;
    background: linear-gradient(to right, var(--band-blue) 0, var(--band-blue) 450px, var(--band-light) 450px, var(--band-blue) 748px);
  }
  .name-band__name {
    position: absolute;
    left: 34px; top: 3px;
    margin: 0;
    font-size: 33px;
    font-weight: 700;
    font-style: italic;
    line-height: 44px;
    color: var(--ink);
  }

  .contact {
    position: absolute;
    left: 32px; top: 318px;
    margin: 0; padding: 0;
    list-style: none;
  }
  .contact__item {
    display: flex;
    align-items: center;
    gap: 15px;
    height: 26px;
    font-size: 19px;
  }
  .contact__icon { width: 22px; height: 20px; flex: none; }

  .tagline {
    position: absolute;
    left: 418px; top: 314px;
    margin: 0;
    font-size: 19px;
  }
</style>
</head>
<body>
<main class="stage">
  <section class="card card--front">
    <div class="brand">
      <span class="brand__ring"></span>
      <span class="brand__name">Frost &amp; Cinder HVAC/R</span>
    </div>

    <div class="name-band">
      <h1 class="name-band__name">Neil Fardon</h1>
    </div>

    <ul class="contact">
      <li class="contact__item">
        <svg class="contact__icon" viewBox="0 0 22 20" aria-hidden="true">
          <path d="M5 2 L8 2 L9 6 L7 8 Q9 12 13 13 L15 11 L19 12 L19 15 Q18 18 14 17 Q5 14 3 5 Q3 2 5 2 Z" fill="#fff"/>
        </svg>
        <span>778-555-4817</span>
      </li>
      <li class="contact__item">
        <svg class="contact__icon" viewBox="0 0 22 20" aria-hidden="true">
          <g fill="none" stroke="#fff" stroke-width="1.5">
            <circle cx="11" cy="10" r="8.5"/>
            <ellipse cx="11" cy="10" rx="4" ry="8.5"/>
            <line x1="2.5" y1="10" x2="19.5" y2="10"/>
            <line x1="4" y1="5.5" x2="18" y2="5.5"/>
            <line x1="4" y1="14.5" x2="18" y2="14.5"/>
          </g>
        </svg>
        <span>www.frosthvac-example.ca</span>
      </li>
      <li class="contact__item">
        <svg class="contact__icon" viewBox="0 0 22 20" aria-hidden="true">
          <path d="M1 8 L11 1 L21 8 L21 19 L1 19 Z" fill="#fff"/>
          <path d="M1 8 L11 14 L21 8" fill="none" stroke="#000" stroke-width="1.5"/>
        </svg>
        <span>info@frosthvac-example.ca</span>
      </li>
    </ul>

    <p class="tagline">Skilled Precision - Superior Value</p>
  </section>

  <section class="card card--back">
    <div class="brand">
      <span class="brand__ring"></span>
      <span class="brand__name">Frost &amp; Cinder HVAC/R</span>
    </div>
  </section>
</main>
</body>
</html>
```